Financial Sevices firm looking for Brochure design

Our company Dunmere Halcott and Vesk Limited (DunmereVesk)
i
Is an investment/advisory firm - www.dunmerevesk.com
We invest in the energy sector in Africa and offer advisory services to Energy companies looking to invest in Africa. From oil and gas, to renewables (wind/solar). We are more focused on the "West African" Sub region
We need corporate brochure (Booklet style) to circulate to our corporate clients
We would like to see a design that considers the colours in our Logo (see website)
HI Guys, sorry been travelling. Seen some very good submissions and will be sending updates shortly
Reason: Dear Designers,
Thank you for participating in this project and for some of the great designs i've received so far. Unfortunately, due to the holidays, it has been difficult to consult with other members of my team. As a result, the project deadline is extended by about 12 days
I appreciate your understanding in the situation and looking forward to continuing the excellent collaboration in the coming days
Reason: Hi All,
Apologies for the multiple deadline extensions and thanks so much for all the designs which my team and I will be reviewing today and tomorrow.
We will be closing this project tomorrow by 6pm GMT (17th Jan 2014)
Thanks to all those that submitted such wonderful designs and goodluck!!
Project to be closed finally on 17th Jan 2014 at 6pm GMT
Banks, Investment Firms, Energy companies, Private Equity Funds
I have attached a Brochure that I created myself as an example of the type of information required but please also feel free to visit our website www.dunmerevesk.com
Looking for any creative ideas you have to suplement the information provided.
Financial

```html
<!DOCTYPE html>
<html lang="en">
<head>
<meta charset="utf-8">
<title>DunmereVesk Brochure Spread – Values, Mission and Vision</title>
<link rel="stylesheet" href="https://fonts.googleapis.com/css2?family=Exo+2:wght@400;500;700;800&display=swap">
<style>
  :root {
    --backdrop: #1d1d1f;
    --red: #c8161d;
    --red-deep: #9e0f14;
    --orange: #f7a21b;
    --title-red: #8e0d10;
    --text-red: #b5151b;
  }
  * { margin: 0; padding: 0; box-sizing: border-box; }
  html, body {
    width: 1200px; height: 750px; overflow: hidden;
    background: var(--backdrop);
    font-family: "Exo 2", Arial, sans-serif;
  }
  .spread {
    position: absolute; left: 233px; top: 70px;
    width: 859px; height: 606px;
    box-shadow: 0 10px 40px rgba(0,0,0,.6);
  }
  .spread-art { position: absolute; inset: 0; display: block; }

  .values-title {
    position: absolute; left: 2px; top: 196px;
    font-size: 74px; font-weight: 700; letter-spacing: -2px;
    color: var(--title-red); line-height: 1; white-space: nowrap;
  }
  .values-list { list-style: none; }
  .values-list li {
    position: absolute; font-size: 13px; font-weight: 700;
    color: var(--title-red); line-height: 1; white-space: nowrap;
  }
  .values-list .v1 { left: 277px; top: 265px; }
  .values-list .v2 { left: 242px; top: 279px; }
  .values-list .v3 { left: 295px; top: 293px; }
  .values-list .v4 { left: 288px; top: 307px; }

  .statement { position: absolute; left: 560px; width: 200px; height: 102px; }
  .statement.mission { top: 166px; }
  .statement.vision { top: 334px; }
  .statement-label {
    position: absolute; left: 10px; top: 50%;
    transform: translate(-50%, -50%) rotate(-90deg);
    font-size: 9px; font-weight: 700; letter-spacing: .5px;
    color: var(--text-red); white-space: nowrap;
  }
  .statement-bracket { position: absolute; left: 30px; top: 0; width: 14px; height: 102px; }
  .statement-text {
    position: absolute; left: 46px; top: 26px; width: 150px;
    font-size: 7.5px; font-weight: 500; line-height: 15px;
    color: var(--text-red); letter-spacing: .2px;
  }
  .statement.vision .statement-text { top: 22px; }
</style>
</head>
<body>
<main class="spread">
  <svg class="spread-art" viewBox="0 0 859 606" xmlns="http://www.w3.org/2000/svg">
    <defs>
      <radialGradient id="photoTone" cx="30%" cy="50%" r="80%">
        <stop offset="0" stop-color="#3d83b3"/>
        <stop offset=".35" stop-color="#1f5a8c"/>
        <stop offset=".55" stop-color="#6f6d4c"/>
        <stop offset=".75" stop-color="#d9881f"/>
        <stop offset="1" stop-color="#a3470e"/>
      </radialGradient>
      <linearGradient id="bandTone" x1="0" x2="1">
        <stop offset="0" stop-color="#c8161d"/>
        <stop offset=".7" stop-color="#b3131a"/>
        <stop offset="1" stop-color="#e8851a"/>
      </linearGradient>
      <linearGradient id="gutter" x1="0" x2="1">
        <stop offset="0" stop-color="#000" stop-opacity="0"/>
        <stop offset=".5" stop-color="#000" stop-opacity=".28"/>
        <stop offset="1" stop-color="#000" stop-opacity="0"/>
      </linearGradient>
      <linearGradient id="pageFade" x1="0" x2="1">
        <stop offset="0" stop-color="#e4e4e4"/>
        <stop offset=".12" stop-color="#fff"/>
        <stop offset=".85" stop-color="#fff"/>
        <stop offset="1" stop-color="#ececec"/>
      </linearGradient>
    </defs>

    <rect x="430" y="0" width="429" height="606" fill="url(#pageFade)"/>
    <rect x="0" y="0" width="430" height="606" fill="url(#photoTone)" role="img" aria-label="Photograph of a glass globe against a warm orange glow"/>

    <g role="img" aria-label="Red and orange angular decorative band">
      <polygon points="0,0 859,0 859,105 430,80 0,60" fill="url(#bandTone)"/>
      <polygon points="0,530 430,518 859,495 859,606 0,606" fill="url(#bandTone)"/>
    </g>

    <rect x="395" y="0" width="70" height="606" fill="url(#gutter)"/>
  </svg>

  <h1 class="values-title">OUR VALUES</h1>
  <ul class="values-list">
    <li class="v1">team work</li>
    <li class="v2">accountability</li>
    <li class="v3">integrity</li>
    <li class="v4">respect</li>
  </ul>

  <section class="statement mission">
    <h2 class="statement-label">MISSION</h2>
    <svg class="statement-bracket" viewBox="0 0 14 102">
      <path d="M12 3 H8 Q4 3 4 8 V94 Q4 99 8 99 H12" fill="none" stroke="var(--orange)" stroke-width="1.2"/>
      <circle cx="12" cy="3" r="1.8" fill="var(--orange)"/><circle cx="12" cy="99" r="1.8" fill="var(--orange)"/>
    </svg>
    <p class="statement-text">To contribute to the implementation of robust infrastructure towards enhanced socio-economic development in Africa.</p>
  </section>

  <section class="statement vision">
    <h2 class="statement-label">VISION</h2>
    <svg class="statement-bracket" viewBox="0 0 14 102">
      <path d="M12 3 H8 Q4 3 4 8 V94 Q4 99 8 99 H12" fill="none" stroke="var(--orange)" stroke-width="1.2"/>
      <circle cx="12" cy="3" r="1.8" fill="var(--orange)"/><circle cx="12" cy="99" r="1.8" fill="var(--orange)"/>
    </svg>
    <p class="statement-text">To create the greatest value for our clients and investors through the efficient implementation of infrastructure and energy related projects across Africa.</p>
  </section>
</main>
</body>
</html>
```